Design some Business Cards for Bright Harbour Advisory

I'm looking for a business card.
Business name - Bright Harbour Advisory (logo attached)
Details:
Dane Whitlock
dane@homestepsupport.com.au
0491 273 518
I want it to look simple and professional

```html
<!DOCTYPE html>
<html lang="en">
<head>
<meta charset="utf-8">
<title>Bright Harbour Advisory – Business Cards</title>
<link href="https://fonts.googleapis.com/css2?family=Mulish:wght@400;600;700&display=swap" rel="stylesheet">
<style>
  :root {
    --page: #ecebe8;
    --card: #ffffff;
    --band: #6d6e70;
    --band-dark: #4a4b4d;
    --accent-blue: #3a8fd6;
    --accent-green: #8dc63f;
    --logo-grey: #58595b;
    --text-light: #ffffff;
  }
  * { box-sizing: border-box; margin: 0; padding: 0; }
  html, body {
    width: 1200px; height: 912px; overflow: hidden;
    background: var(--page);
    font-family: "Mulish", Arial, sans-serif;
  }
  .sheet { position: relative; width: 1200px; height: 912px; }
  .card {
    position: absolute; left: 250px;
    width: 700px; height: 400px;
    background: var(--card);
    box-shadow: 0 6px 18px rgba(0,0,0,0.12);
    overflow: hidden;
  }
  .card--front { top: 44px; }
  .card--back { top: 468px; }

  .brand {
    position: absolute; display: flex; align-items: center; gap: 14px;
  }
  .brand__mark { width: 18px; height: 18px; background: var(--accent-green); flex: none; }
  .brand__name {
    color: var(--logo-grey); font-weight: 700; font-size: 30px;
    letter-spacing: 1px; line-height: 1.1; text-transform: uppercase;
  }
  .card--front .brand { left: 60px; top: 96px; }
  .card--back .brand { left: 270px; top: 96px; }

  .band {
    position: absolute; right: 0; background: var(--band);
    color: var(--text-light); display: flex; align-items: center;
  }
  .band__rule { position: absolute; right: 0; height: 5px; background: var(--accent-blue); }

  .card--front .band { left: 330px; top: 204px; height: 62px; padding: 0 22px 0 14px; gap: 14px; }
  .card--front .band__rule { left: 350px; top: 266px; }
  .band__icon { width: 30px; height: 30px; flex: none; }
  .contact-lines { font-size: 13px; line-height: 1.55; flex: 1; }
  .contact-phone { display: flex; align-items: center; gap: 8px; font-size: 14px; }
  .contact-phone svg { width: 18px; height: 18px; }

  .person { position: absolute; left: 0; top: 282px; display: flex; gap: 16px; }
  .person__tab { width: 14px; height: 52px; background: var(--band-dark); }
  .person__name { color: var(--accent-green); font-weight: 700; font-size: 27px; line-height: 1.1; }
  .person__role { color: var(--accent-blue); font-weight: 600; font-size: 18px; margin-top: 2px; }

  .card--back .band { left: 250px; top: 226px; height: 56px; padding-left: 28px; font-size: 16px; letter-spacing: 0.3px; }
  .card--back .band__rule { left: 270px; top: 282px; }
</style>
</head>
<body>
<main class="sheet">

  <section class="card card--front" aria-label="Business card front">
    <div class="brand">
      <span class="brand__mark"></span>
      <span class="brand__name">Bright Harbour<br>Advisory</span>
    </div>

    <div class="band">
      <svg class="band__icon" viewBox="0 0 30 30" aria-hidden="true">
        <rect x="5" y="7" width="20" height="13" rx="1" fill="none" stroke="#8dc63f" stroke-width="2"/>
        <path d="M2 23h26" stroke="#8dc63f" stroke-width="2"/>
      </svg>
      <div class="contact-lines">
        <div>dane@homestepsupport.com.au</div>
        <div>www.homestepsupport.com.au</div>
      </div>
      <div class="contact-phone">
        <svg viewBox="0 0 24 24" aria-hidden="true">
          <path d="M6.6 10.8a15 15 0 0 0 6.6 6.6l2.2-2.2c.3-.3.7-.4 1-.2 1.1.4 2.3.6 3.6.6.6 0 1 .4 1 1V20c0 .6-.4 1-1 1A17 17 0 0 1 3 4c0-.6.4-1 1-1h3.5c.6 0 1 .4 1 1 0 1.3.2 2.5.6 3.6.1.3 0 .7-.2 1z" fill="#8dc63f"/>
        </svg>
        <span>0491 273 518</span>
      </div>
    </div>
    <div class="band__rule"></div>

    <div class="person">
      <span class="person__tab"></span>
      <div>
        <div class="person__name">Dane Whitlock</div>
        <div class="person__role">Managing Director</div>
      </div>
    </div>
  </section>

  <section class="card card--back" aria-label="Business card back">
    <div class="brand">
      <span class="brand__mark"></span>
      <span class="brand__name">Bright Harbour<br>Advisory</span>
    </div>
    <div class="band">www.homestepsupport.com.au</div>
    <div class="band__rule"></div>
  </section>

</main>
</body>
</html>
```